Marevanga Wines

A Red Wine Label for future Wine Concept called Marevanga Wine. The back label will have the following words which capture the essence of the wine "I am sworn to the secrecy about the origins of this wine but I can assure you it’s from the best cellars of Africa. Marevanga is an African (Shona) name which loosely means honour, praise or to be held in high exteem. Hold on to your hats because this wine is a whirlwind of flavours. It's dark, spicy and fruity flavours will attack the palate with warm aggression and intent whilst being served with Sadza/ Nsima and roasted beef accompanied with mufushwa (dried vegetables) cooked in grounded nut paste. The inspiring flame, style and mood of an African braai, together with its outlandish flavours popping in and out of the glass, Marevanga will make every serving a gesture of respect and distinction!!!"
Updates

I will be buying wine packed in unbranded bottles then Brand it as Marevanga on my own Marevanga label for some African event theme. The wines will be South African a Shiraz. So I need a back label with message placed in brief and front label for a red wine bottle. I have attached some old labels for the wine so I need a redesign of the l label for have a morden and African feel to it                                   

Please

Target Market(s)

Appeal to general populace and those with an afrocentric feel

Requirements
Must have
• Back and front labels, simplicity
Should not have
• Too many colours

```html
<!DOCTYPE html>
<html lang="en">
<head>
<meta charset="utf-8">
<title>Marevanga Shiraz – Front and Back Labels</title>
<link href="https://fonts.googleapis.com/css2?family=Questrial&family=Montserrat:wght@700&display=swap" rel="stylesheet">
<style>
  :root {
    --page: #ffffff;
    --label-frame: #4b5a3c;
    --label-ground: #231f20;
    --ink-light: #ffffff;
    --accent-yellow: #fdbd17;
    --rule: #e4e4e4;
  }
  * { box-sizing: border-box; margin: 0; padding: 0; }
  html, body {
    width: 807px;
    height: 1200px;
    overflow: hidden;
    background: var(--page);
  }
  .sheet {
    position: relative;
    width: 807px;
    height: 1200px;
  }
  .label {
    position: absolute;
    top: 76px;
    width: 324px;
    height: 443px;
    background: var(--label-ground);
    border: 10px solid var(--label-frame);
    box-shadow: 2px 3px 6px rgba(0,0,0,0.25);
    color: var(--ink-light);
    text-align: center;
    font-family: "Questrial", sans-serif;
  }
  .label--front { left: 79px; }
  .label--back { left: 420px; }
  .label-rule {
    position: absolute;
    top: 530px;
    height: 1px;
    background: var(--rule);
  }
  .label-rule--front { left: 79px; width: 323px; }
  .label-rule--back { left: 420px; width: 324px; }

  /* brand mark stand-in */
  .brand-mark {
    display: flex;
    align-items: center;
    justify-content: center;
    gap: 8px;
    color: var(--accent-yellow);
    font-family: "Questrial", sans-serif;
    letter-spacing: 2px;
  }
  .brand-mark__square {
    width: 12px;
    height: 12px;
    background: var(--accent-yellow);
  }
  .label--front .brand-mark {
    position: absolute;
    top: 105px;
    left: 0; right: 0;
    font-size: 15px;
  }
  .label--back .brand-mark {
    position: absolute;
    top: 400px;
    left: 0; right: 0;
    font-size: 12px;
  }

  .wordmark {
    position: absolute;
    top: 226px;
    left: 0; right: 0;
    font-size: 40px;
    letter-spacing: 1px;
    font-weight: 400;
  }
  .varietal {
    position: absolute;
    top: 312px;
    left: 0; right: 0;
    font-family: "Montserrat", sans-serif;
    font-weight: 700;
    font-size: 19px;
  }
  .origin {
    position: absolute;
    top: 344px;
    left: 0; right: 0;
    font-size: 21px;
  }
  .vintage {
    position: absolute;
    top: 380px;
    left: 0; right: 0;
    font-family: "Montserrat", sans-serif;
    font-weight: 700;
    font-size: 21px;
  }

  .back-title {
    position: absolute;
    top: 30px;
    left: 0; right: 0;
    font-size: 26px;
    letter-spacing: 1px;
  }
  .back-story {
    position: absolute;
    top: 70px;
    left: 17px;
    width: 270px;
    font-size: 10.4px;
    line-height: 18px;
  }
</style>
</head>
<body>
<main class="sheet">
  <section class="label label--front" aria-label="Front label">
    <div class="brand-mark"><span class="brand-mark__square"></span>MAREVANGA</div>
    <h1 class="wordmark">MAREVANGA</h1>
    <p class="varietal">SHIRAZ</p>
    <p class="origin">South Africa</p>
    <p class="vintage">2013</p>
  </section>
  <div class="label-rule label-rule--front"></div>

  <section class="label label--back" aria-label="Back label">
    <h2 class="back-title">MAREVANGA</h2>
    <p class="back-story">"I am sworn to the secrecy about the origins of this wine but I can assure you it’s from the best cellars of Africa. Marevanga is an African (Shona) name which loosely means honour, praise or to be held in high exteem. Hold on to your hats because this wine is a whirlwind of flavours. It's dark, spicy and fruity flavours will attack the palate with warm aggression and intent whilst being served with Sadza/ Nsima and roasted beef accompanied with mufushwa (dried vegetables) cooked in grounded nut paste. The inspiring flame, style and mood of an African braai, together with its outlandish flavours popping in and out of the glass, Marevanga will make every serving a gesture of respect and distinction!!!"</p>
    <div class="brand-mark"><span class="brand-mark__square"></span>MAREVANGA</div>
  </section>
  <div class="label-rule label-rule--back"></div>
</main>
</body>
</html>
```